Zielgruppe
Ich biete Menschen, die in ihrem Beruf hohen Stressbelastungen ausgesetzt sind, schnelle und wirksame Hilfe. Sie können bei mir lernen, langfristig ohne Stress in ihrem Job erfolgreich zu sein.
Mein Angebot nennt sich „Mit Ruhe ans Ziel“. Es besteht aus drei Bausteinen, einem wissenschaftlichem Stresstest, intensiven Kleingruppen-Workshops und individuellem Einzelcoaching.
So kann ich flexibel für jeden die passende Lösungsstrategie zur Stressbewältigung anbieten.
Aufgabenstellung
Farbwelt des Logos Mit Ruhe ans Ziel berücksichtigen
Persönlichen Daten/Adressdaten auf der Vorderseite:
Marlene Wudrich
Personal/Business Coach
Stressmanagement-Trainerin
Beraterin für KALMIS Belastungsschutz by Feuring®
Lindauer Weg 17
10482 Berlin
Tel: (030) 41862270
Mobil: (0173) 2904815
Email: info@mit-ruhe-ans-ziel.de
Text auf der Rückseite:
Mit Ruhe ans Ziel:
Wissenschaftlicher Stresstest KALMIS
Intensive Kleingruppen-Workshops
Individuelles Coaching
www.mit-ruhe-ans-ziel.de

```html
<!DOCTYPE html>
<html lang="de">
<head>
<meta charset="utf-8">
<title>Mit Ruhe ans Ziel – Visitenkarte</title>
<link rel="stylesheet" href="https://fonts.googleapis.com/css2?family=Open+Sans:wght@300;400;600;700&display=swap">
<style>
  :root {
    --brand-green: #7ab648;
    --brand-pink: #b5546f;
    --text-dark: #2b2b2b;
    --text-body: #3a3a3a;
    --canvas-bg: #eff0f2;
    --card-white: #ffffff;
    --card-grey: #c8c8ca;
    --back-text: #eeeeee;
  }
  * { box-sizing: border-box; margin: 0; padding: 0; }
  html, body {
    width: 844px; height: 1200px; overflow: hidden;
    background: var(--canvas-bg);
    font-family: "Open Sans", Arial, sans-serif;
  }
  .sheet { position: relative; width: 844px; height: 1200px; }

  .wordmark {
    position: absolute; display: flex; align-items: center; gap: 12px;
    font-weight: 600; color: var(--brand-green); white-space: nowrap;
  }
  .wordmark__dot {
    width: 14px; height: 14px; border-radius: 50%; background: var(--brand-pink);
  }
  .wordmark--hero { left: 0; right: 0; top: 70px; justify-content: center; font-size: 46px; }
  .wordmark--card { left: 103px; top: 52px; font-size: 40px; }
  .wordmark--card .wordmark__dot { width: 12px; height: 12px; }

  .card {
    position: absolute; left: 102px; width: 640px; height: 414px;
    box-shadow: 0 14px 24px rgba(0,0,0,0.18);
  }
  .card--front { top: 210px; background: var(--card-white); border-left: 6px solid var(--brand-green); }
  .card--back { top: 700px; background: var(--card-grey); }

  .holder { position: absolute; left: 97px; top: 152px; font-size: 17px; font-weight: 600; color: var(--text-dark); }

  .service-list { position: absolute; list-style: none; font-size: 17px; line-height: 25px; }
  .service-list li { position: relative; padding-left: 15px; }
  .service-list li::before {
    content: ""; position: absolute; left: 0; top: 10px;
    width: 7px; height: 7px; border-radius: 50%; background: var(--brand-pink);
  }
  .card--front .service-list { left: 97px; top: 186px; color: var(--text-body); }
  .card--back .service-list { left: 165px; top: 186px; color: var(--back-text); font-weight: 300; }

  .address { position: absolute; left: 73px; top: 332px; font-size: 16px; line-height: 24px; color: var(--text-body); }
  .divider { position: absolute; left: 297px; top: 303px; width: 2px; height: 111px; background: var(--brand-pink); }

  .contact { position: absolute; left: 322px; top: 308px; list-style: none; font-size: 16px; line-height: 24px; color: var(--text-body); }
  .contact li { display: flex; align-items: center; gap: 10px; }
  .contact svg { width: 16px; height: 16px; fill: var(--brand-pink); flex: none; }

  .web { position: absolute; left: 154px; top: 352px; font-size: 21px; font-weight: 600; color: var(--brand-green); }
</style>
</head>
<body>
<main class="sheet">
  <div class="wordmark wordmark--hero"><span class="wordmark__dot"></span>Mit Ruhe ans Ziel</div>

  <section class="card card--front" aria-label="Vorderseite">
    <div class="wordmark wordmark--card"><span class="wordmark__dot"></span>Mit Ruhe ans Ziel</div>
    <p class="holder">Marlene Wudrich</p>
    <ul class="service-list">
      <li>Personal/Business Coach</li>
      <li>Stressmanagement-Trainerin</li>
      <li>Beraterin für KALMIS Belastungsschutz by Feuring®</li>
    </ul>
    <p class="address">Lindauer Weg 17<br>10482 Berlin</p>
    <span class="divider"></span>
    <ul class="contact">
      <li><svg viewBox="0 0 16 16" aria-hidden="true"><path d="M3.5 1l2.5 3-1.5 1.8c.8 2 2.4 3.6 4.4 4.4L10.7 8.7l3 2.5-1.5 3C6.5 14 1.8 9.5 1.5 3z"/></svg>(030) 41862270</li>
      <li><svg viewBox="0 0 16 16" aria-hidden="true"><path d="M4 1h7v14H4zM5.5 3v9h4V3zM7 13h1v1H7z" fill-rule="evenodd"/></svg>(0173) 2904815</li>
      <li><svg viewBox="0 0 16 16" aria-hidden="true"><path d="M1 3h14v10H1zM2 4.2v.3l6 4 6-4v-.3z" fill-rule="evenodd"/></svg>info@mit-ruhe-ans-ziel.de</li>
    </ul>
  </section>

  <section class="card card--back" aria-label="Rückseite">
    <div class="wordmark wordmark--card"><span class="wordmark__dot"></span>Mit Ruhe ans Ziel</div>
    <ul class="service-list">
      <li>Wissenschaftlicher Stresstest KALMIS</li>
      <li>Intensive Kleingruppen-Workshops</li>
      <li>Individuelles Coaching</li>
    </ul>
    <p class="web">www.mit-ruhe-ans-ziel.de</p>
  </section>
</main>
</body>
</html>
```